NEED LABEL FOR PACKAGED DRINKING WATER BOTTLE

we are a new company who is into manufacturing of packaged drinking water bottles in 200 ml 500 ml and 1000 ml. we already have a label which we are using in our local market but we are introducing our 200ml bottle in inflight catering where our products will be seen, consumed by various age and origin of people who travel on flights. so we want a label which is simple and elegant.the bottle is a square bottle and label size would be 198 mm x 36 mm.you can use the label provided below for reference.and the bottle shape also is provided
Target Market(s)
flight passengers in domestic flights
Industry/Entity Type
It Company
Look and feel

```html
<!DOCTYPE html>
<html lang="en">
<head>
<meta charset="utf-8">
<title>Nivara Packaged Drinking Water Label</title>
<link rel="stylesheet" href="https://fonts.googleapis.com/css2?family=Ribeye&family=Exo+2:wght@600&display=swap">
<style>
  :root {
    --sky-top: #ffffff;
    --sky-bottom: #d6eef9;
    --water-light: #7fd0f1;
    --water-mid: #3eb4e6;
    --water-deep: #1d9bd8;
    --brand-blue: #1b4f9e;
    --symbol-fill: #9fd8f2;
    --label-white: #ffffff;
  }
  html, body {
    margin: 0;
    padding: 0;
    width: 1200px;
    height: 380px;
    overflow: hidden;
    background: var(--sky-top);
  }
  .label {
    position: relative;
    width: 1200px;
    height: 380px;
    overflow: hidden;
  }
  .label__water-scene {
    position: absolute;
    inset: 0;
    background:
      radial-gradient(ellipse 260px 70px at 190px 175px, rgba(62, 180, 230, 0.55), rgba(62, 180, 230, 0) 100%),
      radial-gradient(ellipse 240px 90px at 1040px 260px, rgba(29, 155, 216, 0.5), rgba(29, 155, 216, 0) 100%),
      linear-gradient(180deg,
        var(--sky-top) 0%,
        var(--sky-bottom) 46%,
        var(--water-light) 52%,
        var(--water-mid) 78%,
        var(--water-deep) 100%);
  }
  .label__symbol {
    position: absolute;
    left: 524px;
    top: 22px;
    width: 152px;
    height: 152px;
  }
  .label__brand {
    position: absolute;
    left: 0;
    right: 0;
    top: 150px;
    margin: 0;
    text-align: center;
    font-family: "Ribeye", serif;
    font-weight: 400;
    font-size: 168px;
    line-height: 1;
    letter-spacing: 0;
    color: var(--brand-blue);
  }
  .label__product {
    position: absolute;
    left: 0;
    right: 0;
    top: 336px;
    margin: 0;
    text-align: center;
    font-family: "Exo 2", sans-serif;
    font-weight: 600;
    font-size: 34px;
    line-height: 1;
    letter-spacing: 2px;
    color: var(--label-white);
    text-shadow: 0 0 6px rgba(29, 155, 216, 0.8);
  }
</style>
</head>
<body>
  <main class="label">
    <div class="label__water-scene" role="img" aria-label="Splashing blue water wave with bubbles across a bright sky"></div>
    <svg class="label__symbol" viewBox="0 0 152 152" role="img" aria-label="Brand symbol">
      <circle cx="76" cy="76" r="76" fill="var(--symbol-fill)"/>
    </svg>
    <h1 class="label__brand">NIVARA</h1>
    <p class="label__product">PACKAGED DRINKING WATER</p>
  </main>
</body>
</html>
```